Daniel Fordyce Psychotherapy Business Card Design Project

I need a welcoming business card for a Somatic Psychotherapy private practice based in Melbourne, Australia. I help individual clients to work through issues in their life that are inhibiting achieving their full potential. I would like a san serif font and the oculars are:
blue: R:37 G:61 B:95 C:93 M:77 Y:38 K:28
orange: R:241 G:103 B:43 C:0 M:74 Y:93 K:0
The final design should communicate warm, welcoming and safe environment in which clients are supported to grow. It should also convey a collaborative approach to achieve success between me (the therapist) and the client. The uploaded file is my new logo. Also an organic look and feel while maintaining professionalism and a clean, simple look is sought after.
In addition to the logo my details are:
Daniel Fordyce
Psychotherapist
B.Arts., Grad Dip. T&D., Dip.Som.Psych, MRTOB, MFLENG
0417 552 908
dfordyce@danielfordyce.com.au
www.danielfordyce.com.au
Psychotherapy Clients
Environment

```html
<!DOCTYPE html>
<html lang="en">
<head>
<meta charset="UTF-8">
<title>Daniel Fordyce Psychotherapy – Business Card</title>
<link rel="stylesheet" href="https://fonts.googleapis.com/css2?family=Montserrat:wght@400;500;600;700&display=swap">
<style>
  :root {
    --brand-blue: #253d5f;
    --brand-orange: #f1672b;
    --card-white: #ffffff;
    --backdrop: #e6e4e1;
    --text-light: #ffffff;
  }
  * { margin: 0; padding: 0; box-sizing: border-box; }
  html, body {
    width: 1200px;
    height: 502px;
    overflow: hidden;
  }
  body {
    background: var(--backdrop);
    font-family: "Montserrat", sans-serif;
    position: relative;
  }
  .card {
    position: absolute;
    top: 77px;
    width: 532px;
    height: 326px;
    border-radius: 16px;
    overflow: hidden;
    box-shadow: 0 2px 6px rgba(0,0,0,0.18);
  }
  .card-front { left: 51px; background: var(--card-white); }
  .card-back  { left: 617px; background: var(--brand-blue); }

  .front-bands {
    position: absolute;
    inset: 0;
    width: 532px;
    height: 326px;
  }

  .wordmark {
    position: absolute;
    font-weight: 600;
    line-height: 1;
  }
  .wordmark .practice {
    display: block;
    letter-spacing: 3.2px;
  }
  .front-wordmark {
    left: 60px;
    top: 46px;
    color: var(--brand-blue);
    font-size: 40px;
    letter-spacing: -0.5px;
  }
  .front-wordmark .practice {
    font-size: 20px;
    margin-top: 6px;
    letter-spacing: 3.6px;
  }

  .contact {
    position: absolute;
    left: 0;
    width: 100%;
    text-align: center;
    color: var(--text-light);
  }
  .contact-name {
    top: 220px;
    font-size: 19px;
    font-weight: 700;
  }
  .contact-name .role { font-weight: 500; }
  .contact-credentials {
    top: 254px;
    font-size: 9.5px;
    font-weight: 500;
    letter-spacing: 0.2px;
  }
  .contact-phone {
    top: 277px;
    font-size: 18px;
    font-weight: 600;
  }

  .back-wordmark {
    left: 0;
    width: 100%;
    top: 190px;
    text-align: center;
    color: var(--text-light);
    font-size: 32px;
  }
  .back-wordmark .practice {
    font-size: 16px;
    margin-top: 6px;
  }
  .website {
    position: absolute;
    left: 0;
    width: 100%;
    top: 292px;
    text-align: center;
    color: var(--text-light);
    font-size: 13px;
    font-weight: 700;
  }
  .website .domain { font-weight: 400; }
</style>
</head>
<body>

  <section class="card card-front" aria-label="Business card front">
    <svg class="front-bands" viewBox="0 0 532 326" aria-hidden="true">
      <path d="M0,146 Q266,112 532,140 L532,326 L0,326 Z" fill="var(--brand-orange)"/>
      <path d="M0,170 Q266,128 532,160 L532,326 L0,326 Z" fill="var(--brand-blue)"/>
    </svg>

    <p class="wordmark front-wordmark">Daniel Fordyce<span class="practice">PSYCHOTHERAPY</span></p>

    <p class="contact contact-name">Daniel Fordyce <span class="role">| Psychotherapist</span></p>
    <p class="contact contact-credentials">B.Arts., Grad Dip. T&amp;D., Dip.Som.Psych, MRTOB, MFLENG</p>
    <p class="contact contact-phone">Ph : 0417 552 908</p>
  </section>

  <section class="card card-back" aria-label="Business card back">
    <p class="wordmark back-wordmark">Daniel Fordyce<span class="practice">PSYCHOTHERAPY</span></p>
    <p class="website">www.danielfordyce<span class="domain">.com.au</span></p>
  </section>

</body>
</html>
```